Heronby Mortgage Capital Business Card

We need a business card design for our mortgage servicing company. In addition to servicing the loans of homeowners, we help homeowners with purchasing their homes and any mortgage refinancing. We would like to see designs that use the colors in the logo attached below (gold-ish yellow and navy blue), and any other design you deem fit! The design should communicate a simpler life with smart mortgages provided by Heronby.

```html
<!DOCTYPE html>
<html lang="en">
<head>
<meta charset="utf-8">
<title>Heronby Mortgage Capital – Business Card</title>
<link href="https://fonts.googleapis.com/css2?family=Arimo:wght@400;700&display=swap" rel="stylesheet">
<style>
  :root {
    --navy: #1f1b5c;
    --navy-deep: #18154a;
    --gold: #d9a52c;
    --paper: #f5f5f3;
    --white: #ffffff;
    --backdrop: #55575a;
  }
  * { box-sizing: border-box; margin: 0; padding: 0; }
  html, body { width: 1200px; height: 1108px; overflow: hidden; }
  body {
    background: var(--backdrop);
    font-family: "Arimo", Arial, sans-serif;
    display: flex;
    flex-direction: column;
    align-items: center;
    justify-content: center;
    gap: 64px;
  }
  .card {
    position: relative;
    width: 620px;
    height: 354px;
    overflow: hidden;
    border-bottom: 4px solid var(--gold);
    box-shadow: 0 10px 30px rgba(0,0,0,.35);
  }

  /* Front */
  .card-front { background: var(--paper); }
  .card-front .wave-band {
    position: absolute;
    left: 0; right: 0; bottom: 0;
    height: 58%;
    background: var(--navy);
    border-top: 3px solid var(--gold);
  }
  .brand {
    color: var(--gold);
    font-weight: 700;
    line-height: 1;
    text-align: center;
  }
  .card-front .brand {
    position: absolute;
    top: 36px;
    right: 48px;
  }
  .brand-name { display: block; font-size: 58px; letter-spacing: -1px; }
  .brand-sub  { display: block; font-size: 18px; letter-spacing: 3px; margin-top: 4px; text-transform: uppercase; }

  .details {
    position: absolute;
    left: 0; right: 0; bottom: 44px;
    display: flex;
    justify-content: center;
    align-items: center;
    gap: 20px;
  }
  .person { text-align: right; color: var(--white); font-size: 13px; line-height: 1.35; }
  .person-name { color: var(--gold); font-weight: 700; font-size: 22px; margin-bottom: 2px; }
  .divider { width: 1px; height: 96px; background: var(--white); opacity: .8; }
  .contacts { list-style: none; color: var(--white); font-size: 13px; line-height: 1.75; }
  .contacts li { display: flex; align-items: center; gap: 10px; }
  .contacts svg { width: 13px; height: 13px; flex: none; }

  /* Back */
  .card-back {
    background: var(--navy);
    display: flex;
    flex-direction: column;
    align-items: center;
    justify-content: center;
    gap: 38px;
  }
  .card-back .brand-name { font-size: 70px; }
  .card-back .brand-sub { font-size: 20px; }
  .tagline { color: var(--white); font-size: 14px; }
</style>
</head>
<body>

<section class="card card-front" aria-label="Business card front">
  <div class="wave-band" role="img" aria-label="Navy band shaped by a large fish silhouette outlined in gold"></div>

  <div class="brand">
    <span class="brand-name">Heronby</span>
    <span class="brand-sub">Mortgage</span>
  </div>

  <div class="details">
    <div class="person">
      <p class="person-name">Daniel Reyes</p>
      <p>President</p>
      <p>4120 Alder Creek Road</p>
      <p>Fairbank, Canada 20817</p>
    </div>
    <span class="divider"></span>
    <ul class="contacts">
      <li>
        <svg viewBox="0 0 24 24" fill="var(--gold)"><path d="M6.6 10.8a15.1 15.1 0 0 0 6.6 6.6l2.2-2.2a1 1 0 0 1 1-.25 11.4 11.4 0 0 0 3.6.57 1 1 0 0 1 1 1V20a1 1 0 0 1-1 1A17 17 0 0 1 3 4a1 1 0 0 1 1-1h3.5a1 1 0 0 1 1 1c0 1.25.2 2.45.57 3.57a1 1 0 0 1-.25 1z"/></svg>
        555-218-4076
      </li>
      <li>
        <svg viewBox="0 0 24 24" fill="none" stroke="var(--gold)" stroke-width="2.4"><rect x="6" y="2" width="12" height="20" rx="2"/><line x1="10" y1="18" x2="14" y2="18"/></svg>
        555-391-7702
      </li>
      <li>
        <svg viewBox="0 0 24 24" fill="none" stroke="var(--gold)" stroke-width="2.4"><rect x="2" y="5" width="20" height="14"/><polyline points="2,5 12,13 22,5"/></svg>
        info@heronbymortgage.com
      </li>
      <li>
        <svg viewBox="0 0 24 24" fill="none" stroke="var(--gold)" stroke-width="2.4"><circle cx="12" cy="12" r="10"/><ellipse cx="12" cy="12" rx="4" ry="10"/><line x1="2" y1="12" x2="22" y2="12"/></svg>
        www.heronbymortgage.com
      </li>
    </ul>
  </div>
</section>

<section class="card card-back" aria-label="Business card back">
  <div class="brand">
    <span class="brand-name">Heronby</span>
    <span class="brand-sub">Mortgage</span>
  </div>
  <p class="tagline">Simpler life with smart mortgages</p>
</section>

</body>
</html>
```